Brava Stone Oven Kitchen (restaurant)

Restaurant with a cool vibe.
We need a refresh of existing site. Appealing to a hip crowd of 25 or older age bracket (mid price to high small town). Constant changes food and cocktail menu. A vibing atmosphere with jazz funk hip music.
Must be able to scale for any device… phone/mobile device super important.
Instagram: @Brava.Linwell
Website: bravalinwell.example

Target Market(s)

25-55 age group

Number of Pages Required

1 page

Font styles to use
Sans Serif

Requirements
Must have
• Simple to navigate. Simplicity is the key to all sophistication.

Links/Buttons
Menu
Gift Cards
Reservations
Take Out
Contact Us
Should not have
• Please, nothing generic looking… no cookie cutter look. Originality

```html
<!DOCTYPE html>
<html lang="en">
<head>
<meta charset="utf-8">
<title>Brava Stone Oven Kitchen</title>
<link rel="stylesheet" href="https://fonts.googleapis.com/css2?family=Poppins:wght@500;600;700&display=swap">
<style>
  :root {
    --white: #ffffff;
    --ink: #111111;
    --overlay: rgba(22, 12, 14, 0.34);
    --mural-red: #c8462a;
    --mural-orange: #e07a3c;
    --mural-blue: #3f7cc4;
    --mural-cream: #e8d6a8;
    --tree-green: #6f9a5a;
    --wood: #6a4c48;
    --wood-dark: #3b2827;
    --chair-red: #cf2a2c;
  }
  * { box-sizing: border-box; margin: 0; padding: 0; }
  html, body { width: 1200px; height: 675px; overflow: hidden; background: #1b1416; }
  body { font-family: "Poppins", sans-serif; color: var(--white); }

  .hero { position: relative; width: 1200px; height: 675px; overflow: hidden; }

  .hero-photo {
    position: absolute; inset: 0;
    background:
      linear-gradient(var(--overlay), var(--overlay)),
      linear-gradient(162deg,
        var(--mural-orange) 0%,
        var(--mural-red) 16%,
        var(--mural-cream) 26%,
        var(--mural-red) 34%,
        var(--mural-blue) 44%,
        var(--tree-green) 52%,
        var(--chair-red) 58%,
        var(--wood) 66%,
        #8a6a62 76%,
        var(--wood-dark) 100%);
  }

  .site-nav { position: absolute; top: 0; left: 0; right: 0; height: 110px; }
  .brand-small {
    position: absolute; left: 72px; top: 38px; text-align: center;
    font-weight: 600; line-height: 1;
  }
  .brand-small .name { display: block; font-size: 28px; letter-spacing: 1px; }
  .brand-small .tag { display: block; font-size: 8px; font-weight: 500; margin-top: 3px; }

  .nav-links {
    position: absolute; left: 470px; top: 51px; width: 590px;
    list-style: none; display: flex; justify-content: space-between;
  }
  .nav-links li { font-size: 13px; font-weight: 600; white-space: nowrap; line-height: 18px; }

  .social-dot {
    position: absolute; top: 50px; width: 20px; height: 20px;
    border: 2px solid var(--white); border-radius: 50%;
  }

  .hero-title {
    position: absolute; left: 0; right: 0; top: 238px; text-align: center;
    font-weight: 600; line-height: 1;
  }
  .hero-title .name { display: block; font-size: 96px; letter-spacing: 4px; }
  .hero-title .tag { display: block; font-size: 30px; font-weight: 500; margin-top: 14px; }

  .order-button {
    position: absolute; left: 445px; top: 414px; width: 310px; height: 50px;
    background: var(--white); color: var(--ink);
    font-size: 13px; font-weight: 700; letter-spacing: 0.2px;
    display: flex; align-items: center; justify-content: center;
  }

  .slide-dots { position: absolute; top: 642px; left: 0; }
  .slide-dots span { position: absolute; top: 0; width: 60px; height: 6px; background: var(--white); }
  .slide-dots span.active { background: var(--ink); }
</style>
</head>
<body>
  <main class="hero">
    <div class="hero-photo" role="img" aria-label="Patio photo: colourful painted mural wall, orange shade sails, trees, red chairs and a long wooden table"></div>

    <header class="site-nav">
      <div class="brand-small"><span class="name">BRAVA</span><span class="tag">Stone Oven Kitchen</span></div>
      <ul class="nav-links">
        <li>Home</li>
        <li>Menu</li>
        <li>Reservations</li>
        <li>Order online</li>
        <li>Gift Cards</li>
        <li>Contact</li>
      </ul>
      <span class="social-dot" style="left:1088px" aria-label="Social link"></span>
      <span class="social-dot" style="left:1133px" aria-label="Social link"></span>
    </header>

    <h1 class="hero-title"><span class="name">BRAVA</span><span class="tag">Stone Oven Kitchen</span></h1>

    <a class="order-button">ORDER ONLINE</a>

    <div class="slide-dots">
      <span class="active" style="left:441px"></span>
      <span style="left:527px"></span>
      <span style="left:612px"></span>
      <span style="left:698px"></span>
    </div>
  </main>
</body>
</html>
```